Velko
trosen
Use same font as used in my logo
Yousef Harbi يوسف حربي
General manager المدير العام
P.O.Box 48735 Riyadh 13542
Saudi Arabia
ص.ب 48735 الرياض 13542
المملكة العربية السعودية
Info@velkohouse.example
www.velkohouse.example
C.R. 1049728513 CC.487139
I want to be design Arabic & English

```html
<!DOCTYPE html>
<html lang="en">
<head>
<meta charset="utf-8">
<title>Velko House – Business Card</title>
<link href="https://fonts.googleapis.com/css2?family=Marcellus&family=Open+Sans:wght@400;600;700&family=Noto+Kufi+Arabic:wght@400;700&display=swap" rel="stylesheet">
<style>
  :root {
    --page: #eceef1;
    --card-white: #ffffff;
    --brand-blue: #2f6aa6;
    --brand-deep: #1f4f86;
    --ink: #3b4a5c;
    --pale: rgba(255,255,255,0.16);
  }
  * { margin: 0; padding: 0; box-sizing: border-box; }
  html, body { width: 1200px; height: 980px; overflow: hidden; }
  body {
    background: var(--page);
    font-family: "Open Sans", Arial, sans-serif;
    position: relative;
  }
  .arabic { font-family: "Noto Kufi Arabic", "Open Sans", sans-serif; direction: rtl; }
  .card {
    position: absolute;
    left: 220px;
    width: 760px;
    height: 434px;
    border-radius: 28px;
    overflow: hidden;
    box-shadow: 0 6px 18px rgba(0,0,0,0.14);
  }
  .card--front { top: 40px; background: var(--card-white); }
  .card--back { top: 506px; background: var(--brand-blue); }
  .card-shapes { position: absolute; inset: 0; width: 100%; height: 100%; }

  .brand { position: absolute; left: 34px; top: 118px; display: flex; align-items: center; gap: 16px; }
  .brand-mark { width: 54px; height: 54px; border-radius: 50%; background: var(--brand-blue); }
  .brand-name {
    font-family: "Marcellus", Georgia, serif;
    font-size: 44px;
    letter-spacing: 1px;
    color: var(--brand-blue);
    line-height: 1;
  }

  .contact-list { position: absolute; left: 36px; top: 192px; list-style: none; }
  .contact-list li {
    display: flex; align-items: center; gap: 9px;
    font-size: 12.5px; color: var(--ink); line-height: 1; height: 21px;
  }
  .contact-list .arabic { font-size: 12px; direction: rtl; }
  .contact-icon { width: 15px; height: 15px; flex: none; }
  .contact-spacer { width: 15px; flex: none; }

  .person { position: absolute; right: 28px; bottom: 20px; text-align: right; line-height: 1.3; }
  .person-name { font-size: 15px; font-weight: 700; color: var(--brand-deep); }
  .person-name.arabic { font-size: 13px; }
  .person-role { font-size: 12px; color: var(--ink); }
  .person-role.arabic { font-size: 11px; }

  .web-vertical {
    position: absolute; left: 22px; top: 396px;
    transform-origin: left top; transform: rotate(-90deg);
    font-size: 15px; letter-spacing: 4px; color: #ffffff; white-space: nowrap;
  }
  .back-emblem {
    position: absolute; right: 70px; top: 87px;
    display: flex; flex-direction: column; align-items: center; gap: 18px;
  }
  .back-emblem-mark { width: 200px; height: 200px; border-radius: 50%; border: 14px solid var(--pale); }
  .back-emblem-name {
    font-family: "Marcellus", Georgia, serif; font-size: 30px; letter-spacing: 2px; color: var(--pale);
  }
</style>
</head>
<body>

<section class="card card--front">
  <svg class="card-shapes" viewBox="0 0 760 434" aria-hidden="true">
    <path d="M0,0 H760 V22 C520,40 240,70 0,110 Z" fill="var(--brand-blue)"/>
    <path d="M760,40 C640,170 500,300 400,434" fill="none" stroke="var(--brand-blue)" stroke-width="3"/>
    <path d="M760,62 C650,185 525,320 440,434 L540,434 C605,335 690,250 760,190 Z" fill="var(--brand-blue)"/>
  </svg>

  <div class="brand">
    <span class="brand-mark"></span>
    <span class="brand-name">VELKO HOUSE</span>
  </div>

  <ul class="contact-list">
    <li>
      <svg class="contact-icon" viewBox="0 0 16 16"><circle cx="8" cy="8" r="8" fill="var(--brand-blue)"/><path d="M8 3.5a3 3 0 0 1 3 3c0 2.2-3 6-3 6s-3-3.8-3-6a3 3 0 0 1 3-3z" fill="#fff"/><circle cx="8" cy="6.5" r="1.1" fill="var(--brand-blue)"/></svg>
      P.O.Box 48735 Riyadh 13542, Saudi Arabia
    </li>
    <li><span class="contact-spacer"></span><span class="arabic">ص.ب 48735 الرياض 13542، المملكة العربية السعودية</span></li>
    <li>
      <svg class="contact-icon" viewBox="0 0 16 16"><circle cx="8" cy="8" r="8" fill="var(--brand-blue)"/><path d="M5 4h2l.8 2-1.2.9a5 5 0 0 0 1.6 1.6l.9-1.2 2 .8v2c-3.8.3-6.4-2.3-6.1-6.1z" fill="#fff"/></svg>
      +966 11 555 0142
    </li>
    <li>
      <svg class="contact-icon" viewBox="0 0 16 16"><circle cx="8" cy="8" r="8" fill="var(--brand-blue)"/><rect x="4.5" y="4" width="7" height="8" fill="#fff"/><path d="M6 6.5h4M6 8.5h4M6 10h2.5" stroke="var(--brand-blue)" stroke-width="0.8"/></svg>
      C.R. 1049728513 &nbsp; CC.487139
    </li>
    <li>
      <svg class="contact-icon" viewBox="0 0 16 16"><circle cx="8" cy="8" r="8" fill="var(--brand-blue)"/><rect x="4" y="5" width="8" height="6" fill="#fff"/><path d="M4 5l4 3.2L12 5" fill="none" stroke="var(--brand-blue)" stroke-width="1"/></svg>
      Info@velkohouse.example
    </li>
    <li>
      <svg class="contact-icon" viewBox="0 0 16 16"><circle cx="8" cy="8" r="8" fill="var(--brand-blue)"/><circle cx="8" cy="8" r="4" fill="none" stroke="#fff" stroke-width="1.1"/><path d="M4 8h8M8 4c-1.6 2.4-1.6 5.6 0 8M8 4c1.6 2.4 1.6 5.6 0 8" fill="none" stroke="#fff" stroke-width="0.9"/></svg>
      www.velkohouse.example
    </li>
  </ul>

  <div class="person">
    <p class="person-name">Yousef Harbi</p>
    <p class="person-role">General manager</p>
    <p class="person-name arabic">يوسف حربي</p>
    <p class="person-role arabic">المدير العام</p>
  </div>
</section>

<section class="card card--back">
  <p class="web-vertical">www.velkohouse.example</p>
  <div class="back-emblem">
    <span class="back-emblem-mark"></span>
    <span class="back-emblem-name">VELKO HOUSE</span>
  </div>
</section>

</body>
</html>
```